Estate Agent/Real Estate valuation tool

We need a design for our our new estate agent valuation tool.

The tool allows users to book a valuation of their house/property with the estate agent, after they choose there property they can then complete their details and choose a booking time.

The mock up of the design we want is attached to this project.(Main Screen)

This also needs to be responsive so the design is easy to use on a mobile device.

Target Market(s)

estate agents

Industry/Entity Type

Real Estate Agent

Number of Pages Required

1 page

Requirements
Must have
• Section 2 and 3 greyed out when user is on step 1
• Section 1 and 3 greyed out when user is on step 2
• Section 1 and 2 greyed out when the user is on step 3
• *** Design must be shown for mobile/ipad and desktop
Nice to have
• Clean and Simple
Should not have
• Dark colours

```html
<!DOCTYPE html>
<html lang="en">
<head>
<meta charset="utf-8">
<title>Book Your Valuation Online – Talvenmere</title>
<link rel="stylesheet" href="https://fonts.googleapis.com/css2?family=Open+Sans:wght@300;400&display=swap">
<style>
  :root {
    --header-top: #0a44d4;
    --header-bottom: #0536a6;
    --footer: #2b6fd1;
    --sky-top: #2e8ee0;
    --sky-mid: #bcd8ef;
    --lawn: #5f9a3a;
    --panel: rgba(255, 255, 255, 0.88);
    --step-active: rgba(228, 228, 234, 0.82);
    --step-idle: rgba(250, 250, 252, 0.55);
    --step-border: #b8b8bc;
    --title: #1f55b8;
    --heading: #2b2b2b;
    --field-text: #1c3a6a;
    --field-bg: #ffffff;
    --field-edge: #d6d6d6;
    --button-bg: #c6d4f8;
    --button-edge: #9eb1df;
    --tab-bg: #ececef;
    --white: #ffffff;
  }
  * { box-sizing: border-box; margin: 0; padding: 0; }
  html, body { width: 1200px; height: 710px; overflow: hidden; }
  body {
    font-family: "Open Sans", Arial, sans-serif;
    position: relative;
    background: var(--white);
  }
  .site-header {
    position: absolute; left: 0; top: 0; width: 1200px; height: 89px;
    background: linear-gradient(var(--header-top), var(--header-bottom));
    border-top: 2px solid #3a6cf0;
    border-bottom: 1px solid #e6ecf8;
    display: flex; align-items: center; justify-content: center;
  }
  .brand-name {
    color: var(--white); font-size: 30px; font-weight: 300; letter-spacing: 1px;
  }
  .hero-backdrop {
    position: absolute; left: 0; top: 89px; width: 1200px; height: 576px;
    background: linear-gradient(180deg, var(--sky-top) 0%, var(--sky-mid) 40%, #d9dde0 62%, var(--lawn) 100%);
  }
  .booking-panel {
    position: absolute; left: 80px; top: 124px; width: 1040px; height: 510px;
    background: var(--panel);
  }
  .booking-title {
    position: absolute; left: 0; top: 38px; width: 100%;
    text-align: center; font-size: 27px; font-weight: 300; color: var(--title);
    line-height: 1;
  }
  .steps {
    position: absolute; left: 8px; top: 89px;
    display: flex; gap: 30px;
  }
  .step {
    width: 321px; height: 373px; border: 1px solid var(--step-border);
    background: var(--step-idle); position: relative;
  }
  .step--active { background: var(--step-active); }
  .step-heading {
    text-align: center; font-size: 18px; font-weight: 300; color: var(--heading);
    margin-top: 27px; line-height: 22px;
  }
  .step-body {
    position: absolute; left: 20px; top: 68px; width: 285px;
    display: flex; flex-direction: column; gap: 12px;
  }
  .field {
    height: 44px; background: var(--field-bg);
    border-top: 2px solid var(--field-edge);
    box-shadow: inset 0 2px 3px rgba(0,0,0,0.08);
    display: flex; align-items: center; justify-content: space-between;
    padding: 0 20px; font-size: 12.5px; color: var(--field-text);
  }
  .field--split { padding: 0; }
  .field--split .field-input { flex: 0 0 186px; padding-left: 20px; height: 100%; display: flex; align-items: center; border-right: 1px solid var(--field-edge); }
  .field--split .field-action { flex: 1; text-align: center; }
  .day-tabs { display: flex; height: 48px; margin-bottom: -2px; }
  .day-tab {
    flex: 1; background: var(--tab-bg); border: 1px solid #c8c8cc; border-radius: 3px;
    font-size: 8px; color: #222; display: flex; align-items: center; justify-content: center;
    white-space: nowrap; overflow: hidden;
  }
  .step-button {
    position: absolute; left: 20px; top: 292px; width: 285px; height: 45px;
    background: var(--button-bg); border: 1px solid var(--button-edge);
    font-size: 16px; color: var(--field-text);
    display: flex; align-items: center; justify-content: center;
  }
  .site-footer {
    position: absolute; left: 0; top: 665px; width: 1200px; height: 45px;
    background: var(--footer); color: var(--white);
    display: flex; align-items: center; justify-content: space-between;
    padding: 0 80px; font-size: 12px;
  }
  .social-links { display: flex; gap: 12px; }
  .social-link { width: 32px; height: 32px; border-radius: 50%; background: var(--white); }
</style>
</head>
<body>
  <header class="site-header">
    <span class="brand-name">TALVENMERE</span>
  </header>

  <div class="hero-backdrop" role="img" aria-label="Photograph of a suburban house with a lawn and hedges under a blue sky"></div>

  <main class="booking-panel">
    <h1 class="booking-title">BOOK YOUR VALUATION ONLINE</h1>
    <div class="steps">
      <section class="step step--active">
        <h2 class="step-heading">PROPERTY DETAILS</h2>
        <div class="step-body">
          <div class="field field--split"><span class="field-input">POSTCODE</span><span class="field-action">SEARCH</span></div>
          <div class="field">123 TEST STREET</div>
          <div class="field">TEST CITY</div>
          <div class="field">TEST COUNTRY</div>
        </div>
        <div class="step-button">PROCEED</div>
      </section>

      <section class="step">
        <h2 class="step-heading">YOUR DETAILS</h2>
        <div class="step-body">
          <div class="field field--split"><span class="field-input">YOUR NAME</span><span class="field-action">SEARCH</span></div>
          <div class="field">YOUR EMAIL</div>
          <div class="field">YOUR CONTACT NO</div>
        </div>
        <div class="step-button">PROCEED</div>
      </section>

      <section class="step">
        <h2 class="step-heading">APPOINMENT TIME</h2>
        <div class="step-body">
          <div class="day-tabs">
            <span class="day-tab">Today</span>
            <span class="day-tab">Tomorrow</span>
            <span class="day-tab">Mon 30th</span>
            <span class="day-tab">Tue 1st</span>
            <span class="day-tab">Wed 2nd</span>
            <span class="day-tab">Thurs 4th</span>
            <span class="day-tab">Fri 5th</span>
          </div>
          <div class="field"><span>SUNDAY 29TH NOVEMBER</span><span>08.30</span></div>
          <div class="field"><span>SUNDAY 29TH NOVEMBER</span><span>10.30</span></div>
          <div class="field"><span>SUNDAY 29TH NOVEMBER</span><span>12.30</span></div>
        </div>
        <div class="step-button">CONFIRM BOOKING</div>
      </section>
    </div>
  </main>

  <footer class="site-footer">
    <span>© 2015 www.talvenmere-valuations.ae | Privacy Policy</span>
    <nav class="social-links" aria-label="Social links">
      <span class="social-link" aria-label="Social profile 1"></span>
      <span class="social-link" aria-label="Social profile 2"></span>
      <span class="social-link" aria-label="Social profile 3"></span>
      <span class="social-link" aria-label="Social profile 4"></span>
    </nav>
  </footer>
</body>
</html>
```